one pager for investors

I will give an initial file in any format needed. Also, the photo that must be included. As well as the logo, that must be the key to the overall design in terms of font, colors, and general layout. I will attach a file in PDF format, which is a one pager presenting a project for investors that I would like to attract and convinced to invest in my project. What I would like you to do is propose me different and better design options, taking my first draft as an example. But you must absolutely keep every single word and number, absolutely all the information written in my first draft(except “ TEMPLATE DRAFT”). Also, on the top left corner is the logo of our company, which I think should be your main inspiration document is a one pager presented to potential investors that not only has to include the most important information in order for them to be able to see everything needed to see the value of the project (which I’ve already taken care of by writing the text needed, numbers presented and timeline shown; all of which which must be preserved in terms of content, but can be completely redesigned and manipulated ) sh a.k.a. Project summary for investor to go for it.
Serious rich investors
Real eatate

```html
<!DOCTYPE html>
<html lang="fr">
<head>
<meta charset="utf-8">
<title>Projet immobilier XXX – Résumé investisseurs</title>
<link href="https://fonts.googleapis.com/css2?family=Montserrat:wght@500;600;700;800&display=swap" rel="stylesheet">
<style>
  :root{
    --stage:#cfcfcf;
    --navy:#0d1f63;
    --yellow:#f8c52f;
    --pink:#e3345a;
    --cyan:#2bb8f2;
    --blue-dark:#0a3f8b;
    --rule:#3b8fd6;
    --white:#ffffff;
  }
  *{margin:0;padding:0;box-sizing:border-box}
  html,body{width:979px;height:1200px;overflow:hidden;background:var(--stage)}
  body{font-family:'Montserrat',sans-serif;position:relative}
  .sheet{position:absolute;left:163.5px;top:138.7px;width:652px;height:923px;background:var(--white)}
  .hero{position:absolute;left:0;top:0;width:652px;height:233px;
    background:linear-gradient(180deg,#c9d6e6 0%,#d9dfe6 35%,#a58a73 60%,#6b6a55 80%,#8a6a4e 100%)}
  .brand{position:absolute;left:0;top:0;width:236px;height:78px;background:var(--white);
    display:flex;align-items:center;gap:10px;padding-left:22px}
  .brand-dot{width:14px;height:14px;border-radius:50%;background:var(--navy);flex:none}
  .brand-name{color:var(--navy);font-weight:700;font-size:16px;white-space:nowrap}
  .title-band{position:absolute;left:0;top:233px;width:652px;height:49px;background:var(--navy);
    color:var(--white);font-weight:700;font-size:25.5px;display:flex;align-items:center;justify-content:center}
  .intro{position:absolute;left:14px;top:295px;width:624px;text-align:center;color:var(--navy);
    font-weight:800;font-size:10.6px;line-height:12.3px}
  .duration{position:absolute;left:0;top:340px;width:652px;text-align:center;color:var(--pink);
    font-weight:700;font-size:21px}
  .section-head{position:absolute;top:376px;height:30px;font-weight:700;font-size:17px;display:flex;align-items:center}
  .head-plan{left:0;width:326px;background:var(--yellow);color:var(--navy);padding-left:32px;
    clip-path:polygon(0 0,100% 0,calc(100% - 16px) 100%,0 100%)}
  .head-structure{left:326px;width:326px;background:var(--pink);color:var(--white);padding-left:17px;
    clip-path:polygon(0 0,100% 0,calc(100% - 12px) 100%,0 100%)}
  .panel{position:absolute;left:0;top:406px;width:652px;height:431px;
    background:linear-gradient(180deg,#0b1d5e 0%,#14306e 45%,#0e2563 100%)}
  .panel-divider{position:absolute;left:327px;top:418px;height:406px;border-left:1px dotted var(--rule)}
  .row{position:absolute;color:var(--white);font-weight:600;font-size:13.4px;line-height:14px}
  .row .value{display:block;font-weight:700;font-size:18px;line-height:19px}
  .row .note{display:block;font-size:13.4px;line-height:15px;margin-top:1px}
  .currency{position:absolute;color:var(--white);font-weight:700;font-size:13.4px}
  .rule{position:absolute;border-top:1px dotted var(--rule)}
  .col-left .rule{left:33px;width:276px}
  .col-right .rule{left:348px;width:276px}
  .timeline{position:absolute;left:0;top:0;width:652px;height:923px;overflow:visible}
  .timeline text{font-family:'Montserrat',sans-serif;fill:var(--white);text-anchor:middle}
  .footer-rule{position:absolute;top:874px;border-top:1px dotted var(--navy)}
  .footer-label{position:absolute;left:0;top:866px;width:652px;text-align:center;color:var(--pink);font-weight:700;font-size:13.5px}
  .footer-address{position:absolute;left:0;top:884px;width:652px;text-align:center;color:var(--navy);font-weight:700;font-size:14px}
  .footer-bar{position:absolute;left:0;top:913px;width:652px;height:10px;background:var(--navy)}
</style>
</head>
<body>
<main class="sheet">
  <div class="hero" role="img" aria-label="Photographie d'un immeuble résidentiel moderne à balcons vitrés entouré d'arbres"></div>
  <div class="brand">
    <span class="brand-dot"></span>
    <span class="brand-name">Veranor Properties SA</span>
  </div>

  <h1 class="title-band">CONFIDENTIEL – Projet imobilier “XXX”</h1>

  <p class="intro">Le projet XXX est un projet de dévloppement de 30 appartements de standing en PPE au centre de Lausanne. Le terrain a été sécurisé par la signature du vente à terme conditionnelle. L’objectif est d’obtenir le permis de construire, puis de ventre les lots. Dans un premier temps sur plan puis au fil de la construction.</p>

  <p class="duration">Durée estimée du projet – 24 à 36 mois.</p>

  <h2 class="section-head head-plan">PLAN FINANCIER</h2>
  <h2 class="section-head head-structure">STRUCTURE D’INVESTISSEMENT</h2>

  <section class="panel"></section>
  <div class="panel-divider"></div>

  <div class="col-left">
    <div class="row" style="left:33px;top:417px">Prix du terrain<span class="value">2’000’000</span></div>
    <span class="currency" style="left:258px;top:420px">CHF</span>
    <div class="rule" style="top:455px"></div>

    <div class="row" style="left:33px;top:464px">Frais d’acquisition<span class="value">100’000</span></div>
    <span class="currency" style="left:258px;top:467px">CHF</span>
    <div class="rule" style="top:502px"></div>

    <div class="row" style="left:33px;top:511px">Coût de construction<span class="value">2’500’000</span></div>
    <span class="currency" style="left:258px;top:514px">CHF</span>
    <div class="rule" style="top:550px"></div>

    <div class="row" style="left:33px;top:558px">Divers &amp; imprévus<span class="value">200’000</span></div>
    <span class="currency" style="left:258px;top:561px">CHF</span>
    <div class="rule" style="top:596px"></div>

    <div class="row" style="left:33px;top:605px">Prix de revient total<span class="value">4’800’000</span></div>
    <span class="currency" style="left:258px;top:608px">CHF</span>
    <div class="rule" style="top:643px"></div>

    <div class="row" style="left:33px;top:652px">Prix de vente total<span class="value">7’500’000</span></div>
    <span class="currency" style="left:258px;top:655px">CHF</span>
    <div class="rule" style="top:691px"></div>

    <div class="row" style="left:33px;top:699px">Honoraires sur vente<span class="value">190’000</span></div>
    <span class="currency" style="left:258px;top:702px">CHF</span>
    <div class="rule" style="top:738px"></div>

    <div class="row" style="left:33px;top:751px">Marge projet<span class="value">2’510’000</span></div>
    <div class="rule" style="top:790px"></div>

    <div class="row" style="left:33px;top:803px">En % sur prix de vente</div>
    <span class="currency" style="left:258px;top:802px">33.47%</span>
  </div>

  <div class="col-right">
    <div class="row" style="left:348px;top:417px">Besoin de fonds propres<span class="value">2’000’000</span></div>
    <span class="currency" style="left:570px;top:420px">CHF</span>
    <div class="rule" style="top:455px"></div>

    <div class="row" style="left:348px;top:464px">Retour de fonds total<span class="value">3’156’600</span></div>
    <span class="currency" style="left:570px;top:467px">CHF</span>
    <div class="rule" style="top:503px"></div>

    <div class="row" style="left:348px;top:511px">Bénéfice net investisseur<span class="value">1’656’600</span><span class="note">Soit 2/3 du bénéfice projet</span></div>
    <span class="currency" style="left:570px;top:514px">CHF</span>
    <div class="rule" style="top:565px"></div>

    <div class="row" style="left:348px;top:572px">Multiple sur fonds propres<span class="value">x1.83</span></div>
    <div class="rule" style="top:611px"></div>

    <div class="row" style="left:348px;top:619px">Rendement annualisé<br>Calcul sur 24 mois</div>
    <span class="currency" style="left:570px;top:629px">41.4%</span>
  </div>

  <svg class="timeline" viewBox="0 0 652 923" aria-label="Calendrier du projet">
    <g>
      <circle cx="409.5" cy="737" r="62" fill="var(--white)"/>
      <circle cx="507" cy="710" r="49" fill="var(--white)"/>
      <circle cx="555" cy="795" r="62" fill="var(--white)"/>
      <circle cx="458" cy="823" r="42" fill="var(--white)"/>
    </g>
    <g>
      <path d="M409.5 683 a54 54 0 1 0 52 68 L481 766 L470 720 A54 54 0 0 0 409.5 683Z" fill="var(--pink)"/>
      <circle cx="409.5" cy="737" r="40" fill="var(--white)"/>
      <circle cx="409.5" cy="737" r="36" fill="var(--pink)"/>
      <text x="409.5" y="733" font-size="12.5" font-weight="700">8.2024</text>
      <text x="409.5" y="744" font-size="7.5" font-weight="600">Achat</text>
      <text x="409.5" y="753" font-size="7.5" font-weight="600">parcelle</text>
    </g>
    <g>
      <path d="M507 668 a42 42 0 1 1 -9 83 L481 766 L470 730 A42 42 0 0 1 507 668Z" fill="var(--yellow)"/>
      <circle cx="507" cy="710" r="31" fill="var(--white)"/>
      <circle cx="507" cy="710" r="28" fill="var(--yellow)"/>
      <text x="507" y="708" font-size="11" font-weight="700">4.2025</text>
      <text x="507" y="716" font-size="5.5" font-weight="600">Mise</text>
      <text x="507" y="724" font-size="5.5" font-weight="600">à l’enquête</text>
    </g>
    <g>
      <path d="M555 741 a54 54 0 1 1 -47 80 L481 766 L520 752 A54 54 0 0 1 555 741Z" fill="var(--cyan)"/>
      <circle cx="555" cy="795" r="38" fill="var(--white)"/>
      <circle cx="555" cy="795" r="34" fill="var(--cyan)"/>
      <text x="555" y="795" font-size="12.5" font-weight="700">12.2025</text>
      <text x="555" y="806" font-size="7.5" font-weight="600">Livraison</text>
    </g>
    <g>
      <path d="M458 785 a38 38 0 1 0 28 12 L481 766Z" fill="var(--blue-dark)"/>
      <circle cx="458" cy="823" r="27" fill="var(--white)"/>
      <circle cx="458" cy="823" r="24.5" fill="var(--blue-dark)"/>
      <text x="458" y="820" font-size="10" font-weight="700">12.2025</text>
      <text x="458" y="828" font-size="5.5" font-weight="600">Début</text>
      <text x="458" y="835" font-size="5.5" font-weight="600">construction</text>
    </g>
    <circle cx="481" cy="766" r="15" fill="var(--white)"/>
  </svg>

  <div class="footer-rule" style="left:0;width:263px"></div>
  <div class="footer-rule" style="left:389px;width:263px"></div>
  <p class="footer-label">CONFIDENTIEL</p>
  <p class="footer-address">Veranor Properties Vaud SA - Chemin des Alpes 12 - CH-1000 Exemple</p>
  <div class="footer-bar"></div>
</main>
</body>
</html>
```